Onboarding Infographic/brochure

We are a small criminal defense firm looking to create some sort of infographic or brochure that we can onboard new clients with. We are currently sending it out via email but want something a bit cooler and fun to send to clients. The information is:

A Few Quick Rules

We are here to help each step of the way. While questions are never discouraged, this letter will answer some of the most common ones we get asked.

Communications

As a client, you should always be in the loop. While we will try to respond to questions as quickly as possible, sometimes we are unable to respond right away. Do not worry - we promise to get back to you soon. Some questions might take some time to research, and a correct answer is better than a quick one.

Appointments

One of the benefits of having an attorney is the ability to discuss your case outside of court, minus the stress and headaches. If you need an appointment, please contact the office.

Appointments must be scheduled in advance. We do not want you to make a special trip to the office only to learn that we are in court or otherwise unavailable.

Jail Visits

If your family member is currently in jail, we take that very seriously. We will visit your loved one and introduce ourselves. While the case is ongoing, we ask that a family member be designated a “contact” person so that messages can be relayed quickly. Never discuss the facts of the case over the phone with someone who is in jail. Jail calls are recorded and we have seen too many cases go south based on remarks made over recorded lines.

Police Reports and Discovery

We will do our best to provide you with copies of everything we receive on your case. Most information will be emailed, so please keep your email address up to date.

Changes in Contact Information

If you move or change numbers during the case, please let us know. It is difficult to help if we are unable to reach you, and helping you is why we are here.

Court Appearances

Cases do not get resolved as quickly as they do on television. Expect there to be several hearings in your case and it may be necessary for you to attend one or more of them. If a hearing is set, you will receive notice of the date and time of each hearing.

Billing and Collections

We understand that this investment was a huge decision for you. As we focus on providing the best representation, we will need for you to stay on schedule with any payment arrangements agreed to at the time of your initial consultation.

Again, thank you for your trust in us. We look forward to getting a fantastic outcome on your case.

Target Market(s)

Criminal defense clients and their families

Industry/Entity Type

Legal

Font styles to use
Serif

Requirements
Must have
• Must incorporate all of the rules we email out. Would like diagrams, images or pictures
Nice to have
• We attached a Welcome brochure. Not sure I want it to look super similar, hence the request for infographic.

```html
<!DOCTYPE html>
<html lang="en">
<head>
<meta charset="utf-8">
<title>A Quick Few Rules</title>
<link href="https://fonts.googleapis.com/css2?family=Dosis:wght@500;600&family=Quicksand:wght@500;600;700&display=swap" rel="stylesheet">
<style>
:root{
  --navy:#2c3a4b;
  --orange:#f7a21b;
  --sky:#8fc9f2;
  --pill:#9dd2f8;
  --mist:#dcedfb;
  --ink:#2d3540;
  --paper:#ffffff;
}
*{margin:0;padding:0;box-sizing:border-box}
html,body{width:1200px;height:2600px;overflow:hidden;background:var(--paper)}
.sheet{position:relative;width:1200px;height:2600px;background:var(--paper);font-family:"Quicksand",sans-serif;color:var(--ink)}
.masthead{position:absolute;left:0;top:0;width:1200px;height:170px;background:var(--navy)}
.masthead h1{position:absolute;left:0;top:22px;width:1200px;text-align:center;font-family:"Dosis",sans-serif;font-weight:500;font-size:70px;letter-spacing:1px;color:var(--orange)}
.intro{position:absolute;left:60px;top:128px;width:1080px;height:90px;border-radius:45px;background:var(--pill);border:5px solid var(--paper);display:flex;align-items:center;justify-content:center;text-align:center;font-weight:600;font-size:23px;line-height:30px;color:var(--navy)}
.rule-title{position:absolute;height:70px;background:var(--navy);color:var(--orange);font-family:"Dosis",sans-serif;font-weight:500;font-size:42px;display:flex;align-items:center;justify-content:center;letter-spacing:.5px}
.rule-title.right{left:380px;width:820px;box-shadow:-14px 14px 0 var(--sky)}
.rule-title.left{left:0;width:820px;box-shadow:14px 14px 0 var(--sky)}
.rule-text{position:absolute;font-size:24.5px;line-height:31px;font-weight:500;color:var(--ink)}
.hl{color:var(--orange)}
.art{position:absolute;border-radius:50% 45% 50% 40%;background:radial-gradient(circle at 50% 55%,#c9e2f7 0%,var(--mist) 60%,#eef6fd 100%)}
.closing{position:absolute;left:0;top:2500px;width:1200px;height:100px;background:var(--navy);color:var(--paper);text-align:center;font-weight:600;font-size:23px;line-height:30px;padding-top:20px}
</style>
</head>
<body>
<main class="sheet">
  <header class="masthead">
    <h1>A QUICK FEW RULES</h1>
  </header>
  <p class="intro">We're here to help each step of the way. While question are never discouraged,<br>this letter will answer most common ones we get asked.</p>

  <section>
    <div class="art" style="left:60px;top:272px;width:240px;height:240px" role="img" aria-label="Illustration of an attorney working at a laptop"></div>
    <h2 class="rule-title right" style="top:268px">Communications</h2>
    <p class="rule-text" style="left:410px;top:372px;width:770px">As a client, you should always be in the loop. while we'll try to respond to questions as quick as possible, sometimes we are unable to respond right away. <span class="hl">Do not worry</span> - we promise to get back to you soon. Some questions might take some time to research, and <span class="hl">a correct answer is better than a quick one</span>.</p>
  </section>

  <section>
    <h2 class="rule-title left" style="top:560px">Appointments</h2>
    <p class="rule-text" style="left:44px;top:670px;width:800px">One of the benefits of having an attorney is the ability to discuss your case outside of court, minus the stress and headaches.<br>If you need a appointment, please contact the office.<br><span class="hl">Appointments must be sceduled in advance.</span><br>We do not want you to make a special trip to the office only to learn that we are in court or otherwise unavailaible.</p>
    <div class="art" style="left:880px;top:600px;width:280px;height:220px" role="img" aria-label="Illustration of a receptionist answering a phone call"></div>
  </section>

  <section>
    <h2 class="rule-title right" style="top:896px">Jail Visits</h2>
    <div class="art" style="left:50px;top:990px;width:320px;height:240px;border-radius:40% 50% 45% 50%" role="img" aria-label="Illustration of a courtroom with a judge and a defendant"></div>
    <p class="rule-text" style="left:410px;top:1000px;width:780px">If your family member is currently in jail, we take that very seriously. We will visit your loved one and introduce ourselves, while the case is ongoing, we ask that family member designated a “contact” person so that messages can be relayed quickly. never discuss the facts of the case over the phone with someone who is in jail.<br><span class="hl">Jail call are recorded</span> and we have seen to may cases go south based on remarks made over recorded lines.</p>
  </section>

  <section>
    <h2 class="rule-title left" style="top:1274px">Police Reports and Discovery</h2>
    <p class="rule-text" style="left:50px;top:1386px;width:800px">We will do our best to <span class="hl">provide you with copies of everything</span> we recieve on your case. most information will be emailed, so <span class="hl">please keep your email address up to date</span>.</p>
    <div class="art" style="left:870px;top:1310px;width:310px;height:226px;border-radius:18px;background:linear-gradient(180deg,#eef6fd,var(--mist))" role="img" aria-label="Illustration of police officers reviewing documents"></div>
  </section>

  <section>
    <div class="art" style="left:90px;top:1570px;width:240px;height:260px;border-radius:20px;background:linear-gradient(180deg,#e4f1fc,var(--mist))" role="img" aria-label="Illustration of a man holding a phone beside an email envelope"></div>
    <h2 class="rule-title right" style="top:1576px;left:400px;width:800px">Change in Contact Information</h2>
    <p class="rule-text" style="left:440px;top:1684px;width:720px">If you <span class="hl">move or change numbers</span> during the case, <span class="hl">please let us know.</span> It is difficult to help if we are unable to reach you, and helping you is why we are here.</p>
  </section>

  <section>
    <h2 class="rule-title left" style="top:1876px;width:800px">Court Appearances</h2>
    <p class="rule-text" style="left:64px;top:1984px;width:780px"><span class="hl">Cases do not get resolved as quickly as they do on TV.</span><br>Expect there to be several hearings in your case and it may be necessary for you to attend one or more of them. If a hearing is set, you will recieve notice of the date and time of each hearing.</p>
    <div class="art" style="left:860px;top:1880px;width:300px;height:260px" role="img" aria-label="Illustration of a woman checking her phone for a hearing notice"></div>
  </section>

  <section>
    <div class="art" style="left:60px;top:2160px;width:300px;height:270px" role="img" aria-label="Illustration of hands making a payment on a phone"></div>
    <h2 class="rule-title right" style="top:2176px">Billing and Collections</h2>
    <p class="rule-text" style="left:400px;top:2282px;width:790px">We understand that this investment was a huge decision for you. As we <span class="hl">focus on providing the best representation</span>, we need for you to <span class="hl">stay on schedule with any payment</span> arrangements agreed to at the time of your initial consultation.</p>
  </section>

  <footer class="closing">Again, thank you for your trust in us.<br>We look forward to getting a fantastic outcome on your case.</footer>
</main>
</body>
</html>
```